Business Card Design Project

In addition to the logo design we want a professional and contemporary business card for a talent management agency. We provide management services to creative artists and want to communicate a professional creative vibe.
Updates

Project Deadline Extended
Reason: Sorry didnt realise I had put such a short timeline on it.

Target Market(s)

The business deals with creative artists and other industry professionals

Industry/Entity Type

Artists

Colors

Designer to choose colors to be used in the design.

Requirements
Must have
• Logo
Address
Phone
Email

```html
<!DOCTYPE html>
<html lang="en">
<head>
<meta charset="utf-8">
<title>Fenwick Artists – Business Card</title>
<link rel="stylesheet" href="https://fonts.googleapis.com/css2?family=Open+Sans:wght@300;400;600;700&display=swap">
<style>
  :root {
    --green: #137a3c;
    --green-dark: #0b5a2a;
    --green-light: #1f8f4b;
    --white: #ffffff;
    --paper: #f4f5f4;
    --grey: #555b57;
    --backdrop: #e6e4df;
  }
  * { box-sizing: border-box; margin: 0; padding: 0; }
  html, body { width: 1200px; height: 1023px; overflow: hidden; }
  body {
    background: var(--backdrop);
    font-family: "Open Sans", Arial, sans-serif;
    position: relative;
  }
  .card {
    position: absolute;
    left: 330px;
    width: 540px;
    height: 328px;
    border-radius: 16px;
    overflow: hidden;
    box-shadow: 0 6px 18px rgba(0,0,0,0.18);
  }
  /* Front */
  .card-front { top: 110px; background: linear-gradient(180deg, var(--white), var(--paper)); }
  .front-band {
    position: absolute; left: 0; right: 0; bottom: 0; height: 112px;
    background: linear-gradient(180deg, var(--green-light), var(--green-dark));
  }
  .brand-name {
    position: absolute; left: 30px; top: 42px;
    color: var(--green); font-weight: 700; font-size: 46px; letter-spacing: -0.5px;
    line-height: 1;
  }
  .tagline {
    position: absolute; left: 30px; right: 0; top: 106px;
    background: var(--green); color: var(--white);
    font-size: 11.5px; font-weight: 600; line-height: 1.4;
    padding: 3px 12px 3px 10px; white-space: nowrap;
  }
  .person { position: absolute; right: 32px; top: 140px; text-align: right; }
  .person-name { color: var(--green); font-weight: 300; font-size: 21px; letter-spacing: 1px; line-height: 1.2; }
  .person-role { color: var(--grey); font-size: 9px; letter-spacing: 1px; margin-top: 3px; }
  .address {
    position: absolute; left: 30px; bottom: 20px; font-style: normal;
    color: var(--white); font-size: 13px; line-height: 1.5;
  }
  .contacts {
    position: absolute; right: 32px; bottom: 20px; list-style: none;
    color: var(--white); font-size: 13px; line-height: 1.5;
  }
  .contacts li { display: flex; align-items: center; gap: 8px; }
  .contacts svg { width: 13px; height: 13px; flex: none; }
  /* Back */
  .card-back {
    top: 585px;
    background: linear-gradient(160deg, var(--green-light), var(--green) 55%, var(--green-dark));
    color: var(--white);
  }
  .back-brand {
    position: absolute; left: 0; right: 0; top: 118px; text-align: center;
    font-weight: 700; font-size: 50px; letter-spacing: -0.5px; line-height: 1;
  }
  .back-web {
    position: absolute; left: 0; right: 0; top: 190px; text-align: center;
    font-size: 13px; letter-spacing: 2.5px;
  }
</style>
</head>
<body>
  <section class="card card-front" aria-label="Business card front">
    <div class="brand-name">Fenwick Artists</div>
    <div class="tagline">Specialising in Acting, Presenting and Creative Professionals</div>
    <div class="person">
      <div class="person-name">MAREN ASHCROFT</div>
      <div class="person-role">DIRECTOR</div>
    </div>
    <div class="front-band">
      <address class="address">
        27 Larch Street<br>Glebe NSW 2037<br>Australia
      </address>
      <ul class="contacts">
        <li><svg viewBox="0 0 14 14"><circle cx="7" cy="7" r="7" fill="#fff"/><rect x="4.5" y="3" width="5" height="8" rx="1" fill="#137a3c"/></svg>0400 555 218</li>
        <li><svg viewBox="0 0 14 14"><circle cx="7" cy="7" r="7" fill="#fff"/><path d="M4.5 3.5l2 .2.4 2-1 .8a5 5 0 0 0 2.6 2.6l.8-1 2 .4.2 2c-4 .5-7.5-3-7-7z" fill="#137a3c"/></svg>(+61 2) 9000 4620</li>
        <li><svg viewBox="0 0 14 14"><circle cx="7" cy="7" r="7" fill="#fff"/><rect x="3.5" y="4.5" width="7" height="5" fill="#137a3c"/><path d="M3.5 4.5L7 7.3l3.5-2.8" stroke="#fff" stroke-width="0.8" fill="none"/></svg>info@fenwickartists.com.au</li>
      </ul>
    </div>
  </section>

  <section class="card card-back" aria-label="Business card back">
    <div class="back-brand">Fenwick Artists</div>
    <div class="back-web">www.fenwickartists.com.au</div>
  </section>
</body>
</html>
```